Design for online reviews widget

Attached is a wireframe of a widget we need designing to display reviews on websites from multiple sources. We need this provided at 3 different sizes including full screen, contained (like the wireframe) and mobile.
You have completely free rein on the styling.
The only elements that should remain untouched are the blue stars (https://www.filquarry.net/s/8vtmwp2291zq4h/kv%20stars.ai?dl=0) and powered by logo at the bottom.
Ignore the menu at the top of the wireframe, this is just from the website the widget will be placed on.
Businesses

```html
<!DOCTYPE html>
<html lang="en">
<head>
<meta charset="utf-8">
<title>Reviews Widget – Contained and Mobile</title>
<link href="https://fonts.googleapis.com/css2?family=Montserrat:wght@400;500;600;700&display=swap" rel="stylesheet">
<style>
  :root {
    --stage: #000000;
    --panel: #f4f4f4;
    --card: #ffffff;
    --ink: #3c3c3c;
    --ink-soft: #6f6f6f;
    --ink-strong: #1c1c1c;
    --star-blue: #3ec2f0;
    --star-gold: #f6b81c;
    --badge-blue: #0b5aa6;
    --accent-green: #3ee27f;
    --verified-green: #2ed66b;
    --nav-circle: rgba(226, 226, 226, 0.75);
    --nav-arrow: #c4c4c4;
    --border: #2a2a2a;
  }
  * { box-sizing: border-box; margin: 0; padding: 0; }
  html, body { width: 1200px; height: 1000px; overflow: hidden; background: var(--stage); }
  body { position: relative; font-family: "Montserrat", sans-serif; color: var(--ink); }

  .widget { position: absolute; background: var(--panel); border-radius: 18px; }
  .widget--contained { left: 100px; top: 66px; width: 542px; height: 867px; }
  .widget--mobile { left: 745px; top: 66px; width: 355px; height: 631px; }

  .abs { position: absolute; }

  .score-label { font-size: 9px; color: var(--ink-strong); }
  .score-stars { display: flex; gap: 6px; }
  .score-stars svg { display: block; }

  .filter { display: flex; border: 1px solid var(--border); border-radius: 4px; background: #fff; }
  .filter__label { flex: 1; display: flex; align-items: center; font-size: 10px; color: var(--ink-strong); border-right: 1px solid var(--border); }
  .filter__toggle { display: flex; align-items: center; justify-content: center; }

  .review-card { position: absolute; background: var(--card); border-radius: 20px; box-shadow: 0 4px 14px rgba(0,0,0,0.08); overflow: hidden; }
  .review-card__source { position: absolute; font-weight: 700; color: var(--ink-strong); }
  .review-card__badge { position: absolute; border-radius: 50%; background: var(--badge-blue); border: 2px solid #fff; box-shadow: 0 0 0 1.5px var(--badge-blue); }
  .review-card__title { position: absolute; font-weight: 600; color: var(--ink); }
  .review-card__body { position: absolute; color: var(--ink-soft); overflow: hidden; }
  .review-card__meta { position: absolute; display: grid; color: var(--ink-strong); }
  .review-card__meta b { font-weight: 700; }
  .review-card__verified { position: absolute; color: var(--verified-green); font-weight: 500; }

  .nav-arrow { position: absolute; border-radius: 50%; background: var(--nav-circle); display: flex; align-items: center; justify-content: center; }

  .load-more { position: absolute; background: var(--accent-green); border-radius: 22px; color: #fff; font-weight: 700; display: flex; align-items: center; }
  .powered { position: absolute; text-align: center; }
  .powered__label { font-size: 8px; color: var(--ink-strong); }
  .powered__brand { display: flex; align-items: center; gap: 5px; font-weight: 700; color: var(--ink-strong); }
  .powered__dot { width: 12px; height: 12px; border-radius: 50%; background: var(--star-blue); }
</style>
</head>
<body>

<svg width="0" height="0" style="position:absolute">
  <defs>
    <symbol id="blue-star" viewBox="0 0 30 30">
      <circle cx="15" cy="15" r="15" fill="var(--star-blue)"/>
      <path d="M15 5.5l2.8 5.9 6.4.8-4.7 4.4 1.2 6.4L15 19.8l-5.7 3.2 1.2-6.4-4.7-4.4 6.4-.8z" fill="#fff"/>
    </symbol>
    <symbol id="gold-star" viewBox="0 0 24 24">
      <path d="M12 1.5l3.2 6.6 7.3 1-5.3 5.1 1.3 7.2L12 18l-6.5 3.4 1.3-7.2L1.5 9.1l7.3-1z" fill="var(--star-gold)"/>
    </symbol>
    <symbol id="caret" viewBox="0 0 16 10">
      <path d="M0 0h16L8 9z" fill="var(--ink-strong)"/>
    </symbol>
    <symbol id="chev-left" viewBox="0 0 20 34">
      <path d="M17 2L3 17l14 15" fill="none" stroke="var(--nav-arrow)" stroke-width="3"/>
    </symbol>
    <symbol id="chev-right" viewBox="0 0 20 34">
      <path d="M3 2l14 15L3 32" fill="none" stroke="var(--nav-arrow)" stroke-width="3"/>
    </symbol>
  </defs>
</svg>

<!-- Contained widget -->
<section class="widget widget--contained" aria-label="Reviews widget, contained size">
  <p class="abs score-label" style="left:86px; top:19px;">Combined Review Score 4.3 out of 5</p>
  <div class="abs score-stars" style="left:86px; top:36px;">
    <svg width="25" height="25"><use href="#blue-star"/></svg>
    <svg width="25" height="25"><use href="#blue-star"/></svg>
    <svg width="25" height="25"><use href="#blue-star"/></svg>
    <svg width="25" height="25"><use href="#blue-star"/></svg>
    <svg width="25" height="25"><use href="#blue-star"/></svg>
  </div>
  <div class="abs filter" style="left:303px; top:27px; width:156px; height:35px;">
    <span class="filter__label" style="padding-left:20px;">Filter results</span>
    <span class="filter__toggle" style="width:46px;"><svg width="14" height="9"><use href="#caret"/></svg></span>
  </div>

  <article class="review-card" style="left:86px; top:85px; width:370px; height:339px;">
    <span class="review-card__source" style="left:36px; top:32px; font-size:13px;">TradeTick</span>
    <span class="review-card__badge" style="left:301px; top:21px; width:32px; height:32px;"></span>
    <h3 class="review-card__title" style="left:36px; top:65px; font-size:20px;">Front door with windows</h3>
    <p class="review-card__body" style="left:36px; top:115px; width:310px; height:104px; font-size:14px; line-height:20.6px;">This is the second time we have used Marlow home Improvements , and the service is amazing! Daniel came round several times as we keep changing our minds and he was so helpful and gave us</p>
    <div class="review-card__meta" style="left:36px; top:241px; grid-template-columns:91px auto; row-gap:4px; font-size:9px;">
      <span><b>Reliablity:</b> 9.38</span><span><b>Courtesy:</b> 10</span>
      <span><b>Tidiness:</b> 9.84</span><span><b>Workmanship:</b> 10</span>
    </div>
    <p class="review-card__verified" style="left:80px; top:300px; font-size:9px;">Verified 28th September 2021 | Located in Elmbridge</p>
  </article>

  <article class="review-card" style="left:86px; top:448px; width:370px; height:339px;">
    <span class="review-card__source" style="left:44px; top:28px; font-size:13px;">Searchly</span>
    <div class="abs" style="left:211px; top:25px; display:flex; gap:1px;">
      <svg width="22" height="22"><use href="#gold-star"/></svg>
      <svg width="22" height="22"><use href="#gold-star"/></svg>
      <svg width="22" height="22"><use href="#gold-star"/></svg>
      <svg width="22" height="22"><use href="#gold-star"/></svg>
      <svg width="22" height="22"><use href="#gold-star"/></svg>
    </div>
    <h3 class="review-card__title" style="left:36px; top:65px; font-size:20px;">Positive: Professionalism,</h3>
    <p class="review-card__body" style="left:36px; top:114px; width:314px; height:124px; font-size:14px; line-height:20.6px;">The team did a good job of replacing a large feature window spanning two floors, as well as the others in my property. They're a professional group who were willing to work out solutions to any problem, especially compared to other</p>
    <p class="review-card__meta" style="left:36px; top:257px; font-size:9px;"><span><b>Service:</b> Window installation</span></p>
    <p class="review-card__verified" style="left:188px; top:300px; font-size:9px;">11 months ago by Owen Hartley</p>
  </article>

  <span class="nav-arrow" style="left:51px; top:391px; width:84px; height:84px;"><svg width="20" height="34"><use href="#chev-left"/></svg></span>
  <span class="nav-arrow" style="left:408px; top:391px; width:84px; height:84px;"><svg width="20" height="34"><use href="#chev-right"/></svg></span>

  <span class="load-more" style="left:86px; top:810px; width:137px; height:38px; padding-left:38px; font-size:10px;">Load more</span>
  <div class="powered" style="left:312px; top:808px;">
    <p class="powered__label">Powered by</p>
    <p class="powered__brand" style="font-size:15px; margin-top:6px;"><span class="powered__dot"></span>ScoreWeave</p>
  </div>
</section>

<!-- Mobile widget -->
<section class="widget widget--mobile" aria-label="Reviews widget, mobile size">
  <p class="abs score-label" style="left:0; width:355px; top:27px; text-align:center; font-size:13px;">Combined Review Score 4.3 out of 5</p>
  <div class="abs score-stars" style="left:94px; top:52px;">
    <svg width="29" height="29"><use href="#blue-star"/></svg>
    <svg width="29" height="29"><use href="#blue-star"/></svg>
    <svg width="29" height="29"><use href="#blue-star"/></svg>
    <svg width="29" height="29"><use href="#blue-star"/></svg>
    <svg width="29" height="29"><use href="#blue-star"/></svg>
  </div>
  <div class="abs filter" style="left:96px; top:103px; width:161px; height:36px;">
    <span class="filter__label" style="padding-left:21px; font-size:12px;">Filter results</span>
    <span class="filter__toggle" style="width:47px;"><svg width="16" height="10"><use href="#caret"/></svg></span>
  </div>

  <article class="review-card" style="left:27px; top:160px; width:302px; height:385px;">
    <span class="review-card__source" style="left:28px; top:24px; font-size:12px;">TradeTick</span>
    <span class="review-card__badge" style="left:258px; top:19px; width:28px; height:28px;"></span>
    <h3 class="review-card__title" style="left:28px; top:58px; width:260px; font-size:15px; line-height:21px;">Front door with windows each side and side window</h3>
    <p class="review-card__body" style="left:28px; top:108px; width:260px; font-size:11.5px; line-height:20.6px;">This is the second time we have used Marlow home Improvements , and the service is amazing! Daniel came round several times as we keep changing our minds and he was so helpful and gave us good advice, and the guys who do the fitting are efficient and tidy . I've got to say the end result is amazing and I have recommended to many of friends . Thanks Marlow</p>
    <div class="review-card__meta" style="left:28px; top:311px; grid-template-columns:108px auto; row-gap:4px; font-size:11px;">
      <span><b>Reliablity:</b> 9.38</span><span><b>Courtesy:</b> 10</span>
      <span><b>Tidiness:</b> 9.84</span><span><b>Workmanship:</b> 10</span>
    </div>
    <p class="review-card__verified" style="left:30px; top:357px; font-size:9px;">Verified 28th September 2021 | Located in Elmbridge</p>
  </article>

  <span class="nav-arrow" style="left:6px; top:329px; width:43px; height:43px;"><svg width="12" height="22"><use href="#chev-left"/></svg></span>
  <span class="nav-arrow" style="left:307px; top:329px; width:43px; height:43px;"><svg width="12" height="22"><use href="#chev-right"/></svg></span>

  <span class="load-more" style="left:27px; top:572px; width:125px; height:35px; padding-left:34px; font-size:10px;">Load more</span>
  <div class="powered" style="left:221px; top:572px;">
    <p class="powered__label">Powered by</p>
    <p class="powered__brand" style="font-size:13px; margin-top:7px;"><span class="powered__dot"></span>ScoreWeave</p>
  </div>
</section>

</body>
</html>
```